Illustration For Couples Game - Fun, Edgy, Smart Design

This is a game for couples that is focused on helping them connect on every level... emotional, mental, spiritual, physical, etc. This image is for the back of the cards. I attached the front and it would be awesome if your design for the back worked with the front. If you don't think your idea will work with the front, I am open to a new idea for a different front.

Target Market(s)

middle class women and men from 25-55

Industry/Entity Type

Online Store

Colors
e34297
b768aa
ec1f27
a54499
e667a6
f04a50

Requirements
Must have
• The background needs to be black. For the coloring, red, white, pink, purple are all great. I don't think colors outside of that will work very well but if you feel inspired with other colors I am somewhat open to other colors. Please have the title "Tender Tricks" then "For Couples" as more of a subtitle. Something that is slightly italic and has some shading or outlining might be great, just so that it looks very professional. The dimensions should be 5 inches tall and 3.5 inches wide (sorry not sure about CM). **Also, please have only CMYK designs, thank you!**
Nice to have
• Smart and creative designs that make people think and have depth is great. I actually ran another contest on another site and narrowed down to a few ideas.
• -I like the image of the heart as a lock with a key unlocking it.
• -Also a light bulb shaped as a heart that is turned on
• -Dandelion seeds with hearts attached to them (see example)
• I am open to other images but I know I like these three for sure.
Should not have
• Not overtly sexual since this has more of an emphasis on emotional intimacy than physical. We have found overtly sexual confuses people.

```html
<!DOCTYPE html>
<html lang="en">
<head>
<meta charset="utf-8">
<title>Tender Tricks for Couples – Card Front and Back</title>
<link rel="stylesheet" href="https://fonts.googleapis.com/css2?family=Great+Vibes&family=Tinos&display=swap">
<style>
  :root {
    --page: #ffffff;
    --ink: #000000;
    --white: #ffffff;
    --red: #ec1f27;
    --pink: #e34297;
    --rose: #e667a6;
    --orchid: #d865b0;
    --peach: #fcd088;
    --shadow: rgba(0, 0, 0, 0.35);
  }
  * { margin: 0; padding: 0; box-sizing: border-box; }
  html, body {
    width: 1200px; height: 1200px; overflow: hidden;
    background: var(--page);
  }
  .canvas { position: relative; width: 1200px; height: 1200px; }
  .card {
    position: absolute; top: 236px;
    width: 508px; height: 728px; overflow: hidden;
    box-shadow: 4px 6px 8px var(--shadow);
  }
  .card-front { left: 70px; background: var(--ink); }
  .card-back { left: 623px; background: var(--peach); }
  .card-art { position: absolute; inset: 0; width: 100%; height: 100%; }

  .title-block {
    position: absolute; left: 0; right: 0; top: 270px;
    text-align: center; font-family: "Great Vibes", cursive;
  }
  .title-main {
    display: block; color: var(--white);
    font-size: 70px; line-height: 1; letter-spacing: 1px;
  }
  .title-for {
    display: block; color: var(--pink);
    font-size: 34px; line-height: 0.8; margin-top: -2px;
  }
  .title-sub {
    display: block; color: var(--pink);
    font-size: 86px; line-height: 0.9; margin-top: -8px;
  }

  .back-title {
    position: absolute; left: 0; right: 0; top: 42px;
    text-align: center; font-family: "Great Vibes", cursive;
    font-size: 64px; color: var(--ink); font-weight: 400;
  }
  .back-body {
    position: absolute; left: 45px; right: 45px; top: 142px;
    font-family: "Tinos", "Times New Roman", serif;
    font-size: 17.4px; line-height: 26px; color: var(--ink);
    text-align: justify; text-align-last: center;
  }
</style>
</head>
<body>
<main class="canvas">

  <section class="card card-front" aria-label="Card front">
    <svg class="card-art" viewBox="0 0 424 606" preserveAspectRatio="none" aria-hidden="false">
      <defs>
        <radialGradient id="knot-glow" cx="50%" cy="50%" r="50%">
          <stop offset="0%" stop-color="#ec1f27"/>
          <stop offset="70%" stop-color="#c5162a"/>
          <stop offset="100%" stop-color="#000000" stop-opacity="0"/>
        </radialGradient>
      </defs>
      <g class="corner-bands" stroke="#ffffff" stroke-width="16" fill="none">
        <line x1="-10" y1="40" x2="40" y2="-10"/>
        <line x1="-10" y1="100" x2="100" y2="-10"/>
        <line x1="434" y1="40" x2="384" y2="-10"/>
        <line x1="434" y1="100" x2="324" y2="-10"/>
        <line x1="-10" y1="566" x2="40" y2="616"/>
        <line x1="-10" y1="506" x2="100" y2="616"/>
        <line x1="434" y1="566" x2="384" y2="616"/>
        <line x1="434" y1="506" x2="324" y2="616"/>
      </g>
      <rect class="knot-heart-top" x="120" y="8" width="184" height="196" rx="70" fill="url(#knot-glow)"
            role="img" aria-label="Interlaced red heart knot ornament with a small pink heart at its centre"/>
      <rect class="knot-heart-bottom" x="120" y="404" width="184" height="196" rx="70" fill="url(#knot-glow)"
            role="img" aria-label="Interlaced red heart knot ornament with a small pink heart at its centre"/>
      <path class="side-drop" d="M0 170 Q30 175 32 205 Q30 232 0 236 Z" fill="#e667a6"/>
      <path class="side-drop" d="M424 170 Q394 175 392 205 Q394 232 424 236 Z" fill="#e34297"/>
      <g class="side-hearts">
        <path d="M82 270 C74 258 60 262 62 274 C64 284 82 292 82 292 C82 292 100 284 102 274 C104 262 90 258 82 270 Z" fill="#e34297"/>
        <path d="M342 270 C334 258 320 262 322 274 C324 284 342 292 342 292 C342 292 360 284 362 274 C364 262 350 258 342 270 Z" fill="#e34297"/>
      </g>
      <g class="chat-bubble">
        <path d="M0 352 H88 Q92 352 92 356 V420 Q92 424 88 424 H62 V448 L40 424 H0 Z" fill="#ec1f27"/>
        <path d="M46 380 C40 368 24 370 26 384 C28 394 46 406 46 406 C46 406 64 394 66 384 C68 370 52 368 46 380 Z" fill="#000000"/>
      </g>
      <g class="chat-bubble">
        <path d="M424 352 H340 Q336 352 336 356 V420 Q336 424 340 424 H352 V448 L374 424 H424 Z" fill="#d865b0"/>
        <path d="M380 380 C374 368 358 370 360 384 C362 394 380 406 380 406 C380 406 398 394 400 384 C402 370 386 368 380 380 Z" fill="#000000"/>
      </g>
      <g class="confetti">
        <circle cx="60" cy="144" r="3" fill="#e667a6"/>
        <circle cx="88" cy="166" r="2" fill="#ec1f27"/>
        <circle cx="345" cy="148" r="3" fill="#e667a6"/>
        <circle cx="366" cy="190" r="2" fill="#ec1f27"/>
        <circle cx="330" cy="205" r="2" fill="#e34297"/>
        <circle cx="95" cy="310" r="2" fill="#ec1f27"/>
        <circle cx="150" cy="350" r="2.5" fill="#e667a6"/>
        <circle cx="350" cy="460" r="3" fill="#e34297"/>
        <circle cx="90" cy="472" r="3" fill="#e667a6"/>
        <circle cx="60" cy="512" r="2" fill="#ec1f27"/>
      </g>
    </svg>
    <h1 class="title-block">
      <span class="title-main">Tender Tricks</span>
      <span class="title-for">for</span>
      <span class="title-sub">Couples</span>
    </h1>
  </section>

  <section class="card card-back" aria-label="Card back">
    <svg class="card-art" viewBox="0 0 424 606" preserveAspectRatio="none" aria-hidden="true">
      <g class="corner-bands" stroke="#ffffff" stroke-width="24" fill="none">
        <line x1="-10" y1="30" x2="30" y2="-10"/>
        <line x1="-10" y1="95" x2="95" y2="-10"/>
        <line x1="434" y1="30" x2="394" y2="-10"/>
        <line x1="434" y1="95" x2="329" y2="-10"/>
        <line x1="-10" y1="576" x2="30" y2="616"/>
        <line x1="-10" y1="511" x2="95" y2="616"/>
        <line x1="434" y1="576" x2="394" y2="616"/>
        <line x1="434" y1="511" x2="329" y2="616"/>
      </g>
    </svg>
    <h2 class="back-title">Appreciate</h2>
    <p class="back-body">Everyone likes to be appreciated. This week focus on becoming aware of your partner’s many contributions to your life. Notice the little and big things and cultivate an intention to appreciate your partner in ways you seldom acknowledge. Is there an appreciation that you stubbornly hold back on because you feel jealous or have other feelings of insecurity around it? Make an extra effort to acknowledge these contributions from your beloved. Practice expressing your gratitude throughout the day whenever you become aware of feeling thankful. In addition, set aside a few minutes as you go to bed to acknowledge at least five of your lover’s gestures, behaviors, words, or acts that made you feel good. If you are having trouble finding things to acknowledge, then focus on why you got together in the first place and then switch your thoughts to a more positive perspective. Once you shift to a more optimistic mindset, there should be plenty of reasons to appreciate your partner.</p>
  </section>

</main>
</body>
</html>
```